Personal Finance Author needs a postcard

Hi there,

I am a Canadian personal finance author and have published a new book called The Wealth Compass.

I teach Millennials how to create a 6-figure portfolio through investing (https://www.dariafelt.com/)

I'm speaking at some conferences so we were going to print some postcards to hand out to attendees with our info and calls-to-action on them.

I am looking for 4x6 (horizontal) postcard (no space needed for shipping label).

Logos, Headshots and Book Cover:
https://files.cloudvaultex.com/folders/8kQpZrT2mWvN4xLbJ7sHdYc3FgA9eUoRi?usp=sharing

Both sides will be full colour. I would like a clean and simple look. Our main sites are www.DariaFelt.com and www.TheWealthCompassBook.com if you want to get a sense of style and design.
I also uploaded a few marketing materials so you can see the existing designs.

Side 1:
Get Instant Access to your Free Resources - main headline

(small bullets underneath)
- The Wealth Compass Checklist
- Financial Worksheets
- Database of Investment Tools

DariaFelt.com/Resources

At the bottom, include "Don't forget to follow Daria Felt on social media:
Linkedin: @dariafelt7
Facebook: @thewealthcompassbook Instagram: @thewealthcompassbook Twitter: @WealthCompassBk"

Side 2:
Headline - Want to work directly with Daria and The Wealth Compass team to help you make your money grow and stay safe?

Work with us to (bullet point list)...
- Hire Daria as a Keynote Speaker
- Teach Financial Literacy Workshops
- Receive Financial Coaching

Want To Learn More About How We Can Help?
DariaFelt.com/Services

Include my contact info:
Daria Felt
Author | Speaker | Investor
daria@thewealthcompassbook.com
416-555-0187

Target Market(s)

Millennials who want to learn how to save and invest their money. I focus on stock market investing, real estate investing and entrepreneurship.

Industry/Entity Type

Financial Service

Font styles to use
Sans Serif

Colors

Designer to choose colors to be used in the design.

Requirements
Must have
• Photo of Daria Felt
• The Wealth Compass logo
• Green, Gold/Yellow to match existing colours
• modern business style postcard

```html
<!DOCTYPE html>
<html lang="en">
<head>
<meta charset="utf-8">
<title>Daria Felt – Services Postcard</title>
<link rel="stylesheet" href="https://fonts.googleapis.com/css2?family=Bebas+Neue&family=Cabin:wght@400;500&family=Open+Sans:wght@600&display=swap">
<style>
  :root {
    --green: #05643a;
    --gold: #ecb73c;
    --white: #ffffff;
    --ink: #141414;
    --ribbon: #f7f7f5;
  }
  * { margin: 0; padding: 0; box-sizing: border-box; }
  html, body { width: 1200px; height: 800px; overflow: hidden; background: var(--green); }
  .postcard {
    position: relative; width: 1200px; height: 800px; overflow: hidden;
    background: var(--green); font-family: "Cabin", sans-serif; color: var(--white);
  }
  .display { font-family: "Bebas Neue", sans-serif; line-height: 1; position: absolute; white-space: nowrap; }

  .eyebrow {
    position: absolute; left: 275px; top: 62px;
    font-family: "Open Sans", sans-serif; font-weight: 600; font-size: 17px;
    letter-spacing: 2.4px; color: var(--gold);
  }
  .name-big { left: 116px; top: 71px; font-size: 200px; color: var(--white); letter-spacing: -2px; }
  .and { left: 493px; top: 131px; font-size: 34px; color: var(--gold); }
  .team-name { left: 496px; top: 162px; font-size: 80px; color: var(--white); letter-spacing: -1.5px; }
  .team-name .team { font-size: 38px; color: var(--gold); letter-spacing: 0; margin-left: 4px; }
  .promise { left: 126px; top: 245px; font-size: 62px; color: var(--gold); letter-spacing: -1.3px; }
  .promise .highlight { color: var(--white); }

  .band-label {
    position: absolute; left: 123px;
    font-family: "Bebas Neue", sans-serif; font-size: 36px; color: var(--ink);
    line-height: 1; letter-spacing: -0.6px; white-space: nowrap;
  }
  .band-label.services { top: 364px; }
  .band-label.learn { top: 569px; letter-spacing: -1px; }

  .offer-list { position: absolute; left: 88px; top: 424px; list-style: none; }
  .offer-list li {
    position: relative; padding-left: 35px; font-size: 26.5px; line-height: 30px; color: var(--white);
  }
  .offer-list li::before {
    content: ""; position: absolute; left: 3px; top: 11px; width: 9px; height: 9px;
    background: var(--gold); transform: rotate(45deg); box-shadow: 2px -2px 0 -1px var(--white);
  }

  .contact {
    position: absolute; left: 123px; top: 624px; font-size: 26.5px; line-height: 30px;
    color: var(--white); font-style: normal;
  }

  .shapes { position: absolute; inset: 0; }
</style>
</head>
<body>
<main class="postcard">
  <svg class="shapes" width="1200" height="800" viewBox="0 0 1200 800" aria-hidden="true">
    <polygon points="0,357 369,357 383,399 0,399" fill="var(--ribbon)"/>
    <polygon points="0,357 369,357 371,362 0,362" fill="var(--gold)"/>
    <rect x="0" y="562" width="880" height="45" fill="var(--gold)"/>
  </svg>

  <p class="eyebrow">WORK DIRECTLY WITH</p>
  <h1 class="display name-big">DARIA</h1>
  <p class="display and">AND</p>
  <p class="display team-name">THE WEALTH COMPASS<span class="team">TEAM</span></p>
  <p class="display promise">TO HELP YOU MAKE YOUR <span class="highlight">MONEY GROW</span> &amp; STAY SAFE?</p>

  <h2 class="band-label services">WORK WITH US TO:</h2>
  <ul class="offer-list">
    <li>Hire Daria as a Keynote Speaker</li>
    <li>Teach Financial Literacy Workshops</li>
    <li>Receive Financial Coaching</li>
  </ul>

  <h2 class="band-label learn">WANT TO LEARN MORE ABOUT HOW WE CAN HELP?</h2>
  <address class="contact">
    Daria Felt<br>
    Author | Speaker | Investor<br>
    daria@thewealthcompassbook.com<br>
    416-555-0187
  </address>

  <svg class="shapes" width="1200" height="800" viewBox="0 0 1200 800">
    <defs>
      <linearGradient id="photoTone" x1="0" y1="0" x2="0" y2="1">
        <stop offset="0" stop-color="#2f5a44"/>
        <stop offset="1" stop-color="#1c2620"/>
      </linearGradient>
    </defs>
    <rect class="portrait-area" role="img"
          aria-label="Photo of Daria Felt in a dark blazer, smiling and holding up her book The Wealth Compass"
          x="655" y="345" width="545" height="455" fill="url(#photoTone)"/>
  </svg>
</main>
</body>
</html>
```